Sleek business card design for digital agency.

Brief document attached for detailed description and inspiration. Looking for a minimalist sleek, cool, modern business card design.

Industry/Entity Type

Digital

```html
<!DOCTYPE html>
<html lang="en">
<head>
<meta charset="utf-8">
<title>FlintMark Labs – Business Card</title>
<link rel="stylesheet" href="https://fonts.googleapis.com/css2?family=Open+Sans:wght@400;700&display=swap">
<style>
  :root {
    --page: #ffffff;
    --card: #0a0c0e;
    --card-edge: #3a3a3a;
    --accent-blue: #35a8df;
    --ink-dark: #1b1b1b;
    --ink-light: #ffffff;
    --mark-grey: #55514f;
  }
  html, body {
    margin: 0;
    padding: 0;
    width: 924px;
    height: 1200px;
    overflow: hidden;
    background: var(--page);
    font-family: "Open Sans", Arial, sans-serif;
  }
  .sheet {
    position: relative;
    width: 924px;
    height: 1200px;
  }
  .card {
    position: absolute;
    left: 0;
    width: 922px;
    height: 564px;
    background: var(--card);
    border: 1px solid var(--card-edge);
    overflow: hidden;
  }
  .card--front { top: 0; }
  .card--back { top: 634px; }

  .brand {
    position: absolute;
    left: 330px;
    top: 418px;
    display: flex;
    align-items: center;
    gap: 22px;
  }
  .brand__dot {
    width: 56px;
    height: 56px;
    border-radius: 50%;
    background: var(--mark-grey);
  }
  .brand__name {
    font-size: 56px;
    font-weight: 700;
    color: var(--mark-grey);
    letter-spacing: 0.5px;
    line-height: 1;
  }

  .back-art {
    position: absolute;
    inset: 0;
  }
  .contact {
    position: absolute;
    left: 74px;
    top: 0;
    color: var(--ink-light);
  }
  .contact p { margin: 0; position: absolute; left: 0; white-space: nowrap; }
  .contact__name {
    top: 104px;
    font-size: 37px;
    font-weight: 700;
    color: var(--ink-dark);
  }
  .contact__role { top: 155px; font-size: 25px; }
  .contact__line { font-size: 28px; }
</style>
</head>
<body>
<main class="sheet">
  <section class="card card--front">
    <div class="brand">
      <span class="brand__dot"></span>
      <span class="brand__name">FlintMark Labs</span>
    </div>
  </section>

  <section class="card card--back">
    <svg class="back-art" width="922" height="564" viewBox="0 0 922 564">
      <defs>
        <radialGradient id="mark-glow" cx="40%" cy="35%" r="70%">
          <stop offset="0" stop-color="#3c3838"/>
          <stop offset="1" stop-color="#151515"/>
        </radialGradient>
      </defs>
      <path class="back-art__sweep" fill="var(--accent-blue)"
            d="M0 0 H126 C330 60 520 220 574 420 C588 480 570 530 552 564 H0 Z"/>
      <circle role="img" aria-label="Large brand mark symbol" cx="722" cy="240" r="170" fill="url(#mark-glow)"/>
    </svg>
    <div class="contact">
      <p class="contact__name">Daniel Hartley</p>
      <p class="contact__role">Marketing Director</p>
      <p class="contact__line" style="top:226px">Level 3, 18 Carrow St</p>
      <p class="contact__line" style="top:267px">East Brinton NSW 5000</p>
      <p class="contact__line" style="top:309px">0400 555 218</p>
      <p class="contact__line" style="top:350px">03 9000 5123</p>
      <p class="contact__line" style="top:418px">dhartley@flintmarklabs.com</p>
      <p class="contact__line" style="top:458px">@dhartley81</p>
      <p class="contact__line" style="top:500px">facebook.com/FlintMarkLabs</p>
    </div>
  </section>
</main>
</body>
</html>
```